Business Card Design

We like to use greens as you will see in our logo (but not TOO much green). We are a Dental Clinic in a somewhat eccentric community. We do not like the dated sharp designs which we see many dentists use. We're looking for something bright and fresh while still maintaining the integrity of the profession. Elegance is not necessarily what we are going for... we need for the design to be "mature" but also up-lifting.

See our logo.
Updates

Project Deadline Extended
Reason: We have 5 designs which we like. But we'd like to see a few more before committing to a design.

Project Deadline Extended
Reason: We are awaiting revisions to this project. We are still welcoming designs while we wait to see if designers are able to provide to us the revisions we require in order to proceed with a selection.

Target Market(s)

Younger families - ages late 20's to early 40's

Industry/Entity Type

Business

Contact Information for Business Card

Marlow T. Venn DDS 2737 S. Fennimore Ave. Ste. 8 Royal Oak, MI 48059 (248)555-0174 FX (248)555-0189 info@BrightwaveDentalMi.example BrigthwaveDentalMi.example on the back of the card we need an appointment reminder (For____ Date___ Time____) with "If you are unable to keep your appointment, kindly give 48 hours notice" at the bottom. No use of teeth in the design. DOUBLE SIDED DESIGN

Requirements
Should not have
• The use of pictures of teeth

```html
<!DOCTYPE html>
<html lang="en">
<head>
<meta charset="utf-8">
<title>Brightwave Dental Care – Business Card</title>
<link href="https://fonts.googleapis.com/css2?family=Questrial&display=swap" rel="stylesheet">
<style>
  :root {
    --page-bg: #e9ece6;
    --card-bg: #ffffff;
    --green-bright: #5cbf1c;
    --green-soft: #9fd66f;
    --green-line: #b9e08f;
    --green-dark: #1d7a36;
    --text-light: #ffffff;
  }
  * { box-sizing: border-box; margin: 0; padding: 0; }
  html, body { width: 1200px; height: 900px; overflow: hidden; }
  body {
    background: var(--page-bg);
    font-family: "Questrial", "Century Gothic", sans-serif;
    position: relative;
  }
  .card {
    position: absolute;
    top: 161px;
    width: 330px;
    height: 578px;
    background: var(--card-bg);
    overflow: hidden;
    box-shadow: 0 6px 20px rgba(0,0,0,0.15);
  }
  .card--front { left: 215px; }
  .card--back { left: 655px; }
  .card__waves { position: absolute; left: 0; top: 0; width: 330px; height: 578px; }

  /* front */
  .brand { position: absolute; top: 40px; left: 0; width: 100%; text-align: center; color: var(--green-dark); }
  .brand__mark { display: inline-block; width: 26px; height: 26px; border-radius: 50%; background: var(--green-soft); vertical-align: middle; margin-right: 6px; }
  .brand__name { font-size: 30px; vertical-align: middle; letter-spacing: -0.5px; }
  .brand__sub { display: block; font-size: 13px; letter-spacing: 2px; margin-top: 2px; }
  .rule-vertical { position: absolute; left: 180px; top: 105px; width: 2px; height: 180px; background: var(--green-line); }
  .rule-horizontal { position: absolute; left: 0; top: 284px; width: 100%; height: 2px; background: var(--green-line); }
  .doctor { position: absolute; left: 0; width: 100%; color: var(--green-dark); }
  .doctor__first { top: 236px; font-size: 40px; }
  .doctor__first .given { position: absolute; right: 158px; }
  .doctor__first .initial { position: absolute; left: 190px; }
  .doctor__last { top: 294px; font-size: 28px; text-align: left; padding-left: 168px; }
  .contact {
    position: absolute; right: 22px; bottom: 30px;
    color: var(--text-light); text-align: right;
    font-size: 14.5px; line-height: 1.35;
  }

  /* back */
  .reminder { position: absolute; top: 70px; left: 36px; right: 26px; color: var(--green-bright); font-size: 13px; }
  .reminder__row { position: absolute; display: flex; align-items: flex-end; width: 220px; }
  .reminder__row span { margin-right: 6px; }
  .reminder__row i { flex: 1; height: 1px; background: var(--green-line); margin-bottom: 3px; }
  .reminder__row--for { top: 70px; left: 0; }
  .reminder__row--date { top: 100px; left: 24px; }
  .reminder__row--time { top: 130px; left: 48px; }
  .notice {
    position: absolute; right: 20px; bottom: 28px; width: 290px;
    color: var(--text-light); text-align: right; font-size: 13.5px; line-height: 1.35;
  }
</style>
</head>
<body>

<section class="card card--front" aria-label="Business card front">
  <svg class="card__waves" viewBox="0 0 330 578" aria-hidden="true">
    <circle cx="270" cy="560" r="190" fill="var(--green-soft)"/>
    <circle cx="40" cy="600" r="180" fill="var(--green-soft)"/>
    <circle cx="190" cy="640" r="250" fill="var(--green-bright)"/>
  </svg>
  <div class="brand">
    <span class="brand__mark"></span><span class="brand__name">Brightwave</span>
    <span class="brand__sub">DENTAL CARE</span>
  </div>
  <div class="rule-vertical"></div>
  <div class="rule-horizontal"></div>
  <div class="doctor doctor__first"><span class="given">Marlow</span><span class="initial">T.</span></div>
  <div class="doctor doctor__last">Venn DDS</div>
  <address class="contact" style="font-style:normal">
    2737 S. Fennimore Ave. Ste. 8 Royal Oak,<br>
    MI 48059 (248)555-0174<br>
    FX (248)555-0189<br>
    E-mail: info@BrightwaveDentalMi.example<br>
    BrigthwaveDentalMi.example
  </address>
</section>

<section class="card card--back" aria-label="Business card back">
  <svg class="card__waves" viewBox="0 0 330 578" aria-hidden="true">
    <circle cx="280" cy="470" r="190" fill="var(--green-soft)"/>
    <circle cx="20" cy="560" r="170" fill="var(--green-soft)"/>
    <circle cx="200" cy="560" r="240" fill="var(--green-bright)"/>
  </svg>
  <div class="reminder">
    <div class="reminder__row reminder__row--for"><span>For</span><i></i></div>
    <div class="reminder__row reminder__row--date"><span>Date</span><i></i></div>
    <div class="reminder__row reminder__row--time"><span>Time</span><i></i></div>
  </div>
  <p class="notice">"If you are unable to keep your appointment, kindly give 48 hours notice"</p>
</section>

</body>
</html>
```